Body therapist needs a business card

I need a card for my business which is teaching trainings in body therapy, the company is called Wexcombe Educational Group. I teach to massage therapists around Australia, South East Asia and the USA. I am attaching my logo which will guide you as to what colours I would like to have you consider. Please consult my website to find out more about what I do. www.corvantela.com.au

My name is Daniel Wexcombe. My phone number is (03) 9417 2608 or 0461753208. email is info@corvantela.com.au

```html
<!DOCTYPE html>
<html lang="en">
<head>
<meta charset="utf-8">
<title>Wexcombe Educational Group – Business Card</title>
<link href="https://fonts.googleapis.com/css2?family=Didact+Gothic&display=swap" rel="stylesheet">
<style>
  :root {
    --brown: #552e1e;
    --red: #b01a1a;
    --paper: #fbfbfb;
    --faint: #ececec;
    --backdrop: #e4e1dd;
    --white: #ffffff;
  }
  * { margin: 0; padding: 0; box-sizing: border-box; }
  html, body { width: 1200px; height: 900px; overflow: hidden; }
  body {
    background: var(--backdrop);
    font-family: "Didact Gothic", "Century Gothic", sans-serif;
    position: relative;
  }
  .card {
    position: absolute;
    width: 620px;
    height: 378px;
    border-radius: 4px;
    overflow: hidden;
    box-shadow: 0 6px 18px rgba(0,0,0,0.18);
  }
  /* Front */
  .card-front { left: 60px; top: 60px; background: var(--paper); }
  .front-decor {
    position: absolute;
    right: 40px; top: -20px;
    width: 220px; height: 220px;
    border-radius: 50%;
    background: var(--faint);
  }
  .brand {
    position: absolute;
    left: 30px; top: 100px;
    display: flex; align-items: center; gap: 10px;
  }
  .brand-dot {
    width: 34px; height: 34px; border-radius: 50%;
    background: var(--brown);
  }
  .brand-name { color: var(--brown); font-size: 17px; }
  .person-name {
    position: absolute;
    left: 30px; top: 160px;
    color: var(--brown);
    font-size: 43px;
    letter-spacing: 1px;
    white-space: nowrap;
  }
  .person-role {
    position: absolute;
    left: 120px; top: 214px;
    color: var(--red);
    font-size: 32px;
    letter-spacing: 1px;
  }
  .contact {
    position: absolute;
    left: 392px; top: 232px;
    border-left: 2px solid var(--brown);
    padding-left: 12px;
    display: grid;
    grid-template-columns: 26px auto;
    column-gap: 10px;
    row-gap: 9px;
    align-items: center;
  }
  .contact svg { width: 24px; height: 24px; fill: var(--brown); }
  .contact-text { color: var(--red); font-size: 14px; line-height: 1.3; }
  .tab {
    position: absolute;
    bottom: 0;
    height: 24px;
    background: var(--brown);
    border-radius: 14px 14px 0 0;
  }
  .tab-left { left: 120px; width: 140px; }
  .tab-right { left: 450px; width: 130px; }

  /* Back */
  .card-back { left: 520px; top: 462px; background: var(--brown); }
  .back-mark {
    position: absolute;
    left: 50%; top: 58px;
    transform: translateX(-50%);
    width: 150px; height: 150px;
    border-radius: 50%;
    background: var(--white);
  }
  .back-name {
    position: absolute;
    left: 0; right: 0; top: 228px;
    text-align: center;
    color: var(--white);
    font-size: 18px;
  }
  .back-url {
    position: absolute;
    left: 0; right: 0; bottom: 34px;
    text-align: center;
    color: var(--white);
    font-size: 25px;
    letter-spacing: 1.5px;
  }
</style>
</head>
<body>

<section class="card card-front">
  <div class="front-decor"></div>

  <div class="brand">
    <span class="brand-dot"></span>
    <span class="brand-name">Wexcombe Educational Group</span>
  </div>

  <h1 class="person-name">Daniel Wexcombe</h1>
  <p class="person-role">Body Therapist</p>

  <div class="contact">
    <svg viewBox="0 0 24 24" aria-hidden="true">
      <path d="M6.6 10.8a15.1 15.1 0 0 0 6.6 6.6l2.2-2.2a1 1 0 0 1 1-.25 11.4 11.4 0 0 0 3.6.57 1 1 0 0 1 1 1V20a1 1 0 0 1-1 1A17 17 0 0 1 3 4a1 1 0 0 1 1-1h3.5a1 1 0 0 1 1 1c0 1.25.2 2.45.57 3.57a1 1 0 0 1-.25 1z"/>
    </svg>
    <p class="contact-text">(03) 9417 2608<br>(04) 6175 3208</p>

    <svg viewBox="0 0 24 24" aria-hidden="true">
      <path d="M2 5h20v14H2z M3.5 6.5 12 13l8.5-6.5" fill="var(--brown)" stroke="var(--paper)" stroke-width="1.2"/>
    </svg>
    <p class="contact-text">info@corvantela.com.au</p>

    <svg viewBox="0 0 24 24" aria-hidden="true">
      <path d="M4 3l16 8-7 2-3 7z"/>
    </svg>
    <p class="contact-text">www.corvantela.com.au</p>
  </div>

  <div class="tab tab-left"></div>
  <div class="tab tab-right"></div>
</section>

<section class="card card-back">
  <div class="back-mark"></div>
  <p class="back-name">Wexcombe Educational Group</p>
  <p class="back-url">www.corvantela.com.au</p>
</section>

</body>
</html>
```